Company business card

We need a new business card design. We are IT company which is specialized for outsourcing of operations hardware and software (specially Velbrandt, we are a partner), developing custom applications and web applications, BPM solutions, auditing hw and sw. actually design was attached. But we need completely NEW.

Industry/Entity Type

Business

```html
<!DOCTYPE html>
<html lang="sk">
<head>
<meta charset="utf-8">
<title>KOVANT – business card</title>
<link rel="stylesheet" href="https://fonts.googleapis.com/css2?family=Montserrat:wght@700&family=Source+Sans+3:wght@400;600&display=swap">
<style>
  :root {
    --backdrop: #8a8b8b;
    --paper: #e7e7e7;
    --brand-blue: #1f71b1;
    --ink-dark: #2b2b2b;
    --ink-muted: #3c3c3c;
    --white: #ffffff;
    --panel: #e9e9e9;
  }
  * { box-sizing: border-box; margin: 0; padding: 0; }
  html, body {
    width: 1200px; height: 900px; overflow: hidden;
    background: var(--backdrop);
  }
  .canvas { position: relative; width: 1200px; height: 900px; }
  .card {
    position: absolute; left: 321px; width: 507px; height: 290px;
  }
  .card--front { top: 119px; background: var(--paper); }
  .card--back { top: 471px; background: var(--brand-blue); color: var(--white); }

  .front-logo {
    position: absolute; left: 0; right: 0; top: 112px;
    display: flex; align-items: center; justify-content: center; gap: 14px;
  }
  .front-logo__square { width: 56px; height: 56px; background: var(--brand-blue); }
  .wordmark {
    font-family: "Montserrat", sans-serif; font-weight: 700;
    letter-spacing: -0.5px; line-height: 1;
  }
  .front-logo .wordmark { font-size: 42px; color: var(--ink-dark); }
  .front-url {
    position: absolute; left: 0; right: 0; top: 260px; text-align: center;
    font-family: "Source Sans 3", sans-serif; font-size: 12.5px;
    letter-spacing: 4.2px; color: var(--ink-muted);
  }

  .back-info { position: absolute; left: 28px; top: 28px; }
  .back-info .wordmark { font-size: 44px; color: var(--white); }
  .person {
    margin-top: 58px;
    font-family: "Source Sans 3", sans-serif;
  }
  .person__name { font-size: 18px; font-weight: 600; }
  .person__role { font-size: 13.5px; margin-top: 1px; }
  .company {
    margin-top: 10px; font-family: "Source Sans 3", sans-serif;
    font-size: 12.5px; line-height: 18px;
  }
  .contacts {
    list-style: none; margin-top: 6px;
    font-family: "Source Sans 3", sans-serif; font-size: 12.5px;
  }
  .contacts li { display: flex; align-items: center; gap: 7px; height: 19.5px; }
  .contacts svg { width: 13px; height: 13px; flex: none; }
  .back-panel {
    position: absolute; left: 237px; top: 26px; width: 241px; height: 238px;
    background: var(--panel);
  }
</style>
</head>
<body>
<main class="canvas">
  <section class="card card--front" aria-label="Card front">
    <div class="front-logo">
      <span class="front-logo__square"></span>
      <span class="wordmark">KOVANT</span>
    </div>
    <p class="front-url">www.kovant.sk</p>
  </section>

  <section class="card card--back" aria-label="Card back">
    <div class="back-info">
      <p class="wordmark">KOVANT</p>
      <div class="person">
        <p class="person__name">Marek Vondrák</p>
        <p class="person__role">CEO</p>
      </div>
      <p class="company">KOVANT s.r.o.<br>Lipová 12, 811 02 Trnava</p>
      <ul class="contacts">
        <li>
          <svg viewBox="0 0 13 13" aria-hidden="true"><rect x="3" y="0.5" width="7" height="12" rx="1" fill="none" stroke="#fff" stroke-width="1.3"/><rect x="4.5" y="2" width="4" height="7" fill="#fff"/></svg>
          +421 (0) 900 246 810
        </li>
        <li>
          <svg viewBox="0 0 13 13" aria-hidden="true"><rect x="0.7" y="2.7" width="11.6" height="7.8" fill="none" stroke="#fff" stroke-width="1.2"/><path d="M1 3l5.5 4.3L12 3" fill="none" stroke="#fff" stroke-width="1.2"/></svg>
          marek.vondrak@kovant.sk
        </li>
        <li>
          <svg viewBox="0 0 13 13" aria-hidden="true"><circle cx="6.5" cy="6.5" r="5.8" fill="#fff"/><path d="M4 3.5c1.5 0 2 1 1.5 2S3 6.5 4 8.5M8 3c-.5 1.5 1 2 2 2.5M8 10c0-1.5 1-2 2-1.5" fill="none" stroke="#1f71b1" stroke-width="1.2"/></svg>
          www.kovant.sk
        </li>
      </ul>
    </div>
    <div class="back-panel"></div>
  </section>
</main>
</body>
</html>
```